Mobile Friendly Lead Generation Landing Page

We are a web marketing company that specialized in web lead generation. Recently we have started buying media from mobile devices and we need a mobile interface(landing page) where we can collect user data in an effective manner.

Our current mobile landing page is:
http://www.tuitionscout.example.com/lp13d/index.aspx?a=true&source=581406
Through this you can see what the steps/questions users need to answer to get matched to a school. We need the design for the whole process.

We are pretty open for design ideas and our goal is to make this mobile optimized landing page have the look and feel of an app...but not an app.
There are several questions in the process but we are open to changing the way they are presented. As in, you can have one question at a time or a few.
The goal is to make this EXTREMELY EASY for users to interact with.

One example that we have liked is:
http://lessonhub.example/schools/47215-page1.lhub (please note that this opens only on mobile devices)

Some of these screenshots are attached.

Our web form looks like this:
http://www.tuitionscout.example.com/lp88/index.aspx?a=true

```html
<!DOCTYPE html>
<html lang="en">
<head>
<meta charset="utf-8">
<title>Get Matched to Colleges – Mobile Landing</title>
<link rel="stylesheet" href="https://fonts.googleapis.com/css2?family=Montserrat:wght@600;700&display=swap">
<style>
  :root {
    --canvas-bg: #eeeeee;
    --band-green: #84b400;
    --panel-green: #79aa00;
    --headline-white: #ffffff;
    --button-top: #ffffff;
    --button-bottom: #e2e2e2;
    --button-edge: #cfcfcf;
    --start-green: #79aa00;
  }
  * { box-sizing: border-box; margin: 0; padding: 0; }
  html, body {
    width: 1200px;
    height: 900px;
    overflow: hidden;
    background: var(--canvas-bg);
    font-family: "Montserrat", Arial, sans-serif;
  }
  .landing {
    position: absolute;
    left: 336px;
    top: 34px;
    width: 528px;
    height: 832px;
    display: flex;
    flex-direction: column;
    overflow: hidden;
  }
  .hero-photo {
    height: 370px;
    background:
      radial-gradient(ellipse at 30% 65%, rgba(214, 92, 150, 0.55), transparent 55%),
      radial-gradient(ellipse at 78% 45%, rgba(60, 120, 200, 0.55), transparent 50%),
      radial-gradient(ellipse at 55% 40%, rgba(226, 178, 150, 0.8), transparent 60%),
      linear-gradient(180deg, #d9d3cc 0%, #b8a89c 55%, #8d7f78 100%);
  }
  .headline-band {
    height: 162px;
    background: var(--band-green);
    color: var(--headline-white);
    text-align: center;
    padding-top: 28px;
  }
  .headline {
    font-weight: 700;
    font-size: 29px;
    line-height: 32px;
    letter-spacing: 0.3px;
    text-transform: uppercase;
  }
  .subheadline {
    font-weight: 600;
    font-size: 20px;
    margin-top: 12px;
  }
  .action-panel {
    flex: 1;
    background: var(--panel-green);
    padding: 42px 40px 0;
  }
  .start-button {
    display: flex;
    align-items: center;
    justify-content: center;
    width: 443px;
    height: 126px;
    border-radius: 8px;
    border: 1px solid var(--button-edge);
    background: linear-gradient(180deg, var(--button-top) 0%, #f6f6f6 48%, var(--button-bottom) 52%, #ececec 100%);
    box-shadow: 0 3px 5px rgba(0, 0, 0, 0.18);
    color: var(--start-green);
    font-weight: 700;
    font-size: 64px;
    letter-spacing: 1px;
    text-decoration: none;
  }
</style>
</head>
<body>
  <main class="landing">
    <div class="hero-photo" role="img" aria-label="Photo of a smiling group of students giving thumbs up, holding notebooks"></div>
    <section class="headline-band">
      <h1 class="headline">Get Matched to Online<br>&amp; Local Colleges Now</h1>
      <p class="subheadline">Find Online &amp; Campus Colleges</p>
    </section>
    <section class="action-panel">
      <a class="start-button" href="#">START</a>
    </section>
  </main>
</body>
</html>
```